Corvane Supplies Business Card

Professional business card that stand out to our potential customers. Front and back with clean modern design

Industry/Entity Type

Oil and gas

Contact Information for Business Card

Name, address, website , office phone and cell number

Requirements
Must have
• Editable files for each employee

```html
<!DOCTYPE html>
<html lang="en">
<head>
<meta charset="utf-8">
<title>Corvane Supplies Business Card</title>
<link rel="stylesheet" href="https://fonts.googleapis.com/css2?family=Montserrat:wght@400;500;700;800&display=swap">
<style>
  :root {
    --stage: #bdbdbd;
    --card: #231f20;
    --red: #ec1c24;
    --green: #12a14a;
    --cyan: #27b5d8;
    --white: #ffffff;
    --emboss: #2f2b2c;
    --emboss-edge: #3a3637;
  }
  * { box-sizing: border-box; margin: 0; padding: 0; }
  html, body { width: 1200px; height: 815px; overflow: hidden; }
  body {
    background: var(--stage);
    font-family: "Montserrat", sans-serif;
    display: flex;
    align-items: center;
    justify-content: center;
    gap: 36px;
  }
  .card {
    position: relative;
    width: 560px;
    height: 320px;
    background: var(--card);
    border-radius: 22px;
    overflow: hidden;
  }
  .front .corner-tab {
    position: absolute;
    top: 0;
    right: 0;
    width: 40px;
    height: 24px;
    background: var(--red);
  }
  .holder {
    position: absolute;
    top: 46px;
    right: 40px;
    text-align: right;
  }
  .holder-name {
    font-weight: 700;
    font-size: 27px;
    letter-spacing: 1px;
    line-height: 1;
  }
  .holder-name .first { color: var(--red); }
  .holder-name .last { color: var(--green); }
  .holder-role {
    color: var(--white);
    font-size: 12px;
    font-weight: 500;
    margin-top: 6px;
  }
  .divider {
    position: absolute;
    left: 34px;
    right: 40px;
    top: 170px;
    height: 1.5px;
    background: var(--red);
  }
  .brand {
    position: absolute;
    left: 34px;
    top: 122px;
    display: flex;
    align-items: center;
    gap: 10px;
  }
  .brand-square {
    width: 26px;
    height: 26px;
    background: var(--cyan);
  }
  .brand-name {
    color: var(--cyan);
    font-weight: 800;
    font-size: 19px;
    letter-spacing: 1.5px;
    text-transform: uppercase;
  }
  .contacts {
    position: absolute;
    left: 40px;
    top: 186px;
    list-style: none;
  }
  .contacts li {
    display: flex;
    align-items: center;
    gap: 10px;
    color: var(--white);
    font-size: 13px;
    font-weight: 500;
    line-height: 22px;
  }
  .contacts svg { width: 12px; height: 12px; flex: none; }
  .back .brand-mark {
    position: absolute;
    inset: 0;
    display: flex;
    align-items: center;
    justify-content: center;
    gap: 14px;
  }
  .back .brand-square {
    width: 40px;
    height: 40px;
    background: var(--emboss);
    border: 1px solid var(--emboss-edge);
  }
  .back .brand-name {
    color: var(--emboss);
    font-size: 28px;
    letter-spacing: 3px;
  }
</style>
</head>
<body>
  <section class="card front">
    <div class="corner-tab"></div>
    <div class="holder">
      <p class="holder-name"><span class="first">DANIEL</span> <span class="last">FORSYTH</span></p>
      <p class="holder-role">manager</p>
    </div>
    <div class="brand">
      <span class="brand-square"></span>
      <span class="brand-name">Corvane Supplies</span>
    </div>
    <div class="divider"></div>
    <ul class="contacts">
      <li><svg viewBox="0 0 12 12"><path fill="#ec1c24" d="M2.5 1 4.5 1 5.3 3.6 4 4.6C4.7 6 6 7.3 7.4 8L8.4 6.7 11 7.5 11 9.5C11 10.3 10.3 11 9.5 11 5 11 1 7 1 2.5 1 1.7 1.7 1 2.5 1Z"/></svg>1-555-014-0277</li>
      <li><svg viewBox="0 0 12 12"><rect x="0.5" y="2" width="11" height="8" fill="#12a14a"/><path d="M0.5 2 6 7 11.5 2" fill="none" stroke="#231f20" stroke-width="1"/></svg>dforsyth@kelmoreparts.vn</li>
      <li><svg viewBox="0 0 12 12"><circle cx="6" cy="6" r="5.5" fill="#ec1c24"/><path d="M0.5 6H11.5M6 0.5V11.5M2 3.5H10M2 8.5H10" stroke="#231f20" stroke-width="0.8"/></svg>www.kelmoreparts.vn</li>
      <li><svg viewBox="0 0 12 12"><circle cx="6" cy="6" r="5.5" fill="#12a14a"/><path d="M0.5 6H11.5M6 0.5V11.5M2 3.5H10M2 8.5H10" stroke="#231f20" stroke-width="0.8"/></svg>www.kelmoreparts.com</li>
      <li><svg viewBox="0 0 12 12"><path fill="#ec1c24" d="M6 0.5C3.8 0.5 2 2.3 2 4.5 2 7.5 6 11.5 6 11.5S10 7.5 10 4.5C10 2.3 8.2 0.5 6 0.5Z"/><circle cx="6" cy="4.5" r="1.5" fill="#231f20"/></svg>Dalwick Harbor, Vietnam</li>
    </ul>
  </section>

  <section class="card back">
    <div class="brand-mark">
      <span class="brand-square"></span>
      <span class="brand-name">Corvane Supplies</span>
    </div>
  </section>
</body>
</html>
```